Business Card Design

We need a business card design that can also be aplied for postcards. We are a small indie record company that also do consulting, and development of independat artitst . I already have the name and the basic idea of what i am looking for but i am open to any suggestion.
Info for the card
Name of the company : Velmora Records
NAME : Tomas Invaldi
PHONE : 208-5536142
EMAIL : hello@velmorarecords.example
WEB: www.velmorarecords.example
Target Market(s)
Male - Female independent musicians ages 18 to 45
Industry/Entity Type
Record Company
Contact Information for Business Card
Independant records company that also works in consulting for music business models for independent artists
Look and feel
Each slider illustrates characteristics of the customer's brand and the style your logo design should communicate.

```html
<!DOCTYPE html>
<html lang="en">
<head>
<meta charset="utf-8">
<title>Velmora Records — Business Card</title>
<link rel="stylesheet" href="https://fonts.googleapis.com/css2?family=Courier+Prime:wght@400;700&display=swap">
<style>
  :root {
    --backdrop: #8a8a8a;
    --card-front: #0b0b0b;
    --card-back: #f6f6f4;
    --ink: #111111;
    --ink-muted: #6a6a6a;
    --ink-light: #ffffff;
    --shadow: rgba(0, 0, 0, 0.35);
  }
  * { box-sizing: border-box; margin: 0; padding: 0; }
  html, body {
    width: 1200px;
    height: 875px;
    overflow: hidden;
  }
  body {
    background: var(--backdrop);
    font-family: "Courier Prime", "Courier New", monospace;
    position: relative;
  }
  .card {
    position: absolute;
    left: 320px;
    width: 560px;
    height: 320px;
    box-shadow: 0 10px 24px var(--shadow);
    overflow: hidden;
  }
  .card--front { top: 80px; background: var(--card-front); }
  .card--back  { top: 470px; background: var(--card-back); color: var(--ink); }

  .front__photo {
    position: absolute;
    inset: 0;
    background: radial-gradient(ellipse at 35% 60%, #3a3a3a 0%, #1a1a1a 45%, #050505 100%);
  }
  .front__brand {
    position: absolute;
    right: 34px;
    top: 70px;
    text-align: right;
    color: var(--ink-light);
  }
  .front__name {
    font-weight: 700;
    font-size: 40px;
    letter-spacing: 2px;
    line-height: 1.1;
  }
  .front__web {
    font-size: 27px;
    line-height: 1.1;
  }

  .back__person {
    position: absolute;
    left: 36px;
    top: 34px;
    font-weight: 700;
    font-size: 25px;
    letter-spacing: 2px;
    color: var(--ink-muted);
  }
  .back__icon {
    position: absolute;
    width: 22px;
    height: 22px;
  }
  .back__line {
    position: absolute;
    font-size: 22px;
    white-space: nowrap;
  }
  .icon--phone { left: 270px; top: 70px; }
  .line--phone { left: 200px; top: 94px; font-size: 24px; }
  .icon--mail  { left: 266px; top: 128px; width: 28px; }
  .line--mail  { left: 80px; top: 152px; }
  .icon--web   { left: 262px; top: 186px; }
  .line--web   { left: 80px; top: 208px; }
  .line--web2  { left: 150px; top: 236px; }
  .back__brand {
    position: absolute;
    right: 30px;
    bottom: 22px;
    font-weight: 700;
    font-size: 27px;
    letter-spacing: 2px;
    color: var(--ink-muted);
  }
</style>
</head>
<body>
  <section class="card card--front">
    <div class="front__photo" role="img" aria-label="Dark close-up photograph of a record turntable and tonearm"></div>
    <div class="front__brand">
      <div class="front__name">VELMORA RECORDS</div>
      <div class="front__web">www.velmorarecords.example</div>
    </div>
  </section>

  <section class="card card--back">
    <div class="back__person">TOMAS INVALDI</div>

    <svg class="back__icon icon--phone" viewBox="0 0 24 24" aria-hidden="true">
      <path fill="var(--ink)" d="M6.6 2.5c.6-.4 1.4-.3 1.8.3l2.2 3.2c.4.6.3 1.3-.2 1.8l-1.5 1.4c1 2.2 2.7 4 4.9 5.1l1.4-1.5c.5-.5 1.3-.6 1.8-.2l3.2 2.2c.6.4.7 1.2.3 1.8l-1.4 2c-.6.9-1.7 1.3-2.7 1C9.8 17.7 6.3 14.2 4.4 8.6c-.3-1 .1-2.1 1-2.7z"/>
    </svg>
    <div class="back__line line--phone">208-5536142</div>

    <svg class="back__icon icon--mail" viewBox="0 0 28 20" aria-hidden="true">
      <rect x="1" y="1" width="26" height="18" fill="none" stroke="var(--ink)" stroke-width="1.5"/>
      <path d="M1 1 L14 11 L27 1 M1 19 L11 9 M27 19 L17 9" fill="none" stroke="var(--ink)" stroke-width="1.5"/>
    </svg>
    <div class="back__line line--mail">hello@velmorarecords.example</div>

    <svg class="back__icon icon--web" viewBox="0 0 24 24" aria-hidden="true">
      <path fill="var(--ink)" d="M5 2 L5 19 L9 15 L12 22 L15 21 L12 14 L18 14 Z"/>
    </svg>
    <div class="back__line line--web">www.velmorarecords.example</div>
    <div class="back__line line--web2">www.velmorarecords.example</div>

    <div class="back__brand">VELMORA RECORDS</div>
  </section>
</body>
</html>
```